Wholesale food company needs a package for Carp boilies (fishing)

We need a (5kg) doypack with handle design for a new brand here in the BENELUX called Vornel Lures. We already have a logo but we need a flashing design to promote it on shows and webshops. The design must also include some transparant places so you can see the product inside. We have added the logo and the website is www.vornellures.nl. You can look for an impression at http://kestamo-goods.nl/product-category/baits/specials/

Target Market(s)

Carpf fishing and coarse angling

Industry/Entity Type

It Company

Requirements
Must have
• A slogan that suits both types of fishing.
• Extra information doypack:
• Material: PET/PE
• Thickness: 12µ/120µ
• Size: B 320 x H 450 MM

```html
<!DOCTYPE html>
<html lang="en">
<head>
<meta charset="utf-8">
<title>Vornel Lures – Doypack Front and Back</title>
<link href="https://fonts.googleapis.com/css2?family=Stardos+Stencil:wght@700&family=Arimo:wght@400;700&display=swap" rel="stylesheet">
<style>
  :root {
    --sky: #4cc8f0;
    --ocean: #2a4f9f;
    --mid-blue: #3a7cc8;
    --lime: #8cc63f;
    --cyan: #57c3ea;
    --white: #ffffff;
    --ink: #2b2b2b;
    --dim: #cfcfcf;
    --bait-light: #7cf04a;
    --bait-dark: #1f8a18;
  }
  * { box-sizing: border-box; margin: 0; padding: 0; }
  html, body { width: 1200px; height: 892px; overflow: hidden; background: var(--white); }
  .sheet {
    position: relative; width: 1200px; height: 892px;
    border: 1px solid #9a9a9a; background: var(--white);
    font-family: "Arimo", Arial, sans-serif;
  }
  .pouch { position: absolute; top: 25px; width: 508px; height: 820px; }
  .pouch--front { left: 40px; }
  .pouch--back { left: 672px; }
  .pouch__art { position: absolute; inset: 0; width: 508px; height: 820px; display: block; }
  .brand { position: absolute; font-family: "Stardos Stencil", "Stencil", serif; font-weight: 700; line-height: 1; white-space: nowrap; }
  .brand__name { font-size: 54px; letter-spacing: 1px; }
  .brand__line { font-size: 33px; letter-spacing: 1px; margin-top: 6px; }
  .pouch--front .brand { right: 38px; top: 128px; text-align: right; color: var(--white); }
  .pouch--back .brand { left: 26px; top: 133px; color: var(--ink); }
  .claims {
    position: absolute; right: 38px; top: 238px; list-style: none; text-align: right;
    color: var(--white); font-weight: 700; font-size: 16.5px; line-height: 21.5px;
  }
  .seal {
    position: absolute; width: 160px; height: 160px; border-radius: 50%;
    background: var(--white); border: 6px solid var(--lime);
    display: flex; align-items: center; justify-content: center; text-align: center;
    font-family: "Stardos Stencil", "Stencil", serif; font-weight: 700; font-size: 22px; line-height: 1.1;
    color: var(--ocean);
  }
  .pouch--front .seal { left: 80px; top: 575px; }
  .pouch--back .seal { left: 266px; top: 575px; }
  .web { position: absolute; left: 0; width: 508px; text-align: center; font-weight: 700; font-size: 21px; color: var(--ink); }
  .pouch--front .web { top: 772px; left: -9px; }
  .pouch--back .web { top: 780px; left: 0; }
  .label-slot { position: absolute; left: 146px; top: 483px; font-size: 18px; color: var(--ink); }
  .dim { position: absolute; color: var(--dim); font-size: 24px; white-space: nowrap; }
  .dim--v { transform: rotate(-90deg); transform-origin: left top; }
</style>
</head>
<body>
<main class="sheet">

  <span class="dim dim--v" style="left:6px;top:118px;">70mm</span>
  <span class="dim dim--v" style="left:6px;top:492px;">450mm</span>
  <span class="dim dim--v" style="left:638px;top:118px;">70mm</span>
  <span class="dim dim--v" style="left:638px;top:492px;">450mm</span>
  <span class="dim" style="left:247px;top:857px;">320mm</span>
  <span class="dim" style="left:408px;top:857px;">font</span>
  <span class="dim" style="left:878px;top:857px;">320mm</span>
  <span class="dim" style="left:1092px;top:857px;">back</span>

  <!-- Front panel -->
  <section class="pouch pouch--front">
    <svg class="pouch__art" viewBox="0 0 508 820" aria-hidden="false">
      <defs>
        <linearGradient id="tabFront" x1="0" y1="0" x2="1" y2="0">
          <stop offset="0" stop-color="var(--sky)"/><stop offset="1" stop-color="var(--ocean)"/>
        </linearGradient>
        <linearGradient id="bodyFront" x1="0" y1="0" x2="1" y2="1">
          <stop offset="0" stop-color="#3fb4e6"/><stop offset="0.6" stop-color="var(--mid-blue)"/><stop offset="1" stop-color="var(--ocean)"/>
        </linearGradient>
        <radialGradient id="baits" cx="0.4" cy="0.4" r="0.8">
          <stop offset="0" stop-color="var(--bait-light)"/><stop offset="1" stop-color="var(--bait-dark)"/>
        </radialGradient>
      </defs>
      <path class="tab" d="M0,105 V70 A70,70 0 0 1 70,0 H438 A70,70 0 0 1 508,70 V105 Z" fill="url(#tabFront)"/>
      <rect class="tab__hole" x="148" y="13" width="207" height="75" rx="37" fill="var(--white)"/>
      <rect class="body" x="0" y="105" width="508" height="715" fill="url(#bodyFront)"/>
      <polygon points="0,112 388,362 0,300" fill="var(--white)"/>
      <polygon points="0,105 386,358 0,118" fill="var(--cyan)"/>
      <polygon points="0,128 386,360 0,212" fill="var(--lime)"/>
      <polygon points="0,224 386,362 0,262" fill="var(--cyan)"/>
      <polygon points="508,108 508,120 390,360" fill="var(--cyan)"/>
      <polygon points="508,150 508,175 390,362" fill="var(--lime)"/>
      <polygon points="376,362 392,362 508,640 508,700 482,700" fill="var(--white)"/>
      <polygon points="392,368 508,600 508,690 490,690" fill="var(--ocean)"/>
      <polygon points="430,470 508,660 508,700" fill="var(--lime)"/>
      <polygon points="0,292 378,372 486,690 0,690" fill="url(#baits)" stroke="var(--white)" stroke-width="4"
        role="img" aria-label="Photo of bright green boilies filling the clear window"/>
      <rect x="0" y="692" width="508" height="128" fill="var(--white)"/>
      <polygon points="0,730 508,692 508,720 0,765" fill="var(--lime)"/>
      <polygon points="230,708 508,722 508,775" fill="var(--ocean)"/>
      <polygon points="0,772 240,730 0,795" fill="var(--cyan)"/>
    </svg>
    <div class="brand">
      <div class="brand__name">VORNEL LURES</div>
      <div class="brand__line">CARP PRODUCTS</div>
    </div>
    <ul class="claims">
      <li>Eco Friendly</li>
      <li>Premium Quality</li>
      <li>100% Fresh</li>
      <li>High Attraction</li>
    </ul>
    <div class="seal">Vornel<br>Lures</div>
    <p class="web">www.vornellures.nl</p>
  </section>

  <!-- Back panel -->
  <section class="pouch pouch--back">
    <svg class="pouch__art" viewBox="0 0 508 820">
      <defs>
        <linearGradient id="tabBack" x1="0" y1="0" x2="1" y2="0">
          <stop offset="0" stop-color="var(--sky)"/><stop offset="1" stop-color="var(--ocean)"/>
        </linearGradient>
        <linearGradient id="bodyBack" x1="0" y1="0" x2="1" y2="1">
          <stop offset="0" stop-color="#3fb4e6"/><stop offset="0.5" stop-color="var(--mid-blue)"/><stop offset="1" stop-color="var(--ocean)"/>
        </linearGradient>
      </defs>
      <path class="tab" d="M0,105 V70 A70,70 0 0 1 70,0 H438 A70,70 0 0 1 508,70 V105 Z" fill="url(#tabBack)"/>
      <rect class="tab__hole" x="148" y="13" width="207" height="75" rx="37" fill="var(--white)"/>
      <rect x="0" y="105" width="508" height="715" fill="var(--white)"/>
      <polygon points="0,105 508,105 508,122 120,360 0,700 0,820" fill="url(#bodyBack)"/>
      <polygon points="0,105 508,105 508,125 118,356 0,560" fill="url(#bodyBack)"/>
      <polygon points="508,130 508,175 122,358" fill="var(--lime)"/>
      <polygon points="508,218 508,262 124,362" fill="var(--cyan)"/>
      <polygon points="118,360 130,362 0,690 0,600" fill="var(--white)"/>
      <polygon points="122,364 0,640 0,562" fill="var(--lime)"/>
      <polygon points="130,366 0,730 0,670" fill="var(--mid-blue)"/>
      <polygon points="0,700 270,690 270,712 0,740" fill="var(--lime)"/>
      <polygon points="0,820 0,790 270,735" fill="var(--ocean)"/>
      <polygon points="380,700 508,725 508,760" fill="var(--lime)"/>
      <polygon points="370,750 508,770 508,800" fill="var(--cyan)"/>
    </svg>
    <div class="brand">
      <div class="brand__name">VORNEL LURES</div>
      <div class="brand__line">CARP PRODUCTS</div>
    </div>
    <p class="label-slot">here ingredients lable come.</p>
    <div class="seal">Vornel<br>Lures</div>
    <p class="web">www.vornellures.nl</p>
  </section>

</main>
</body>
</html>
```